Korvell Plant Services

We are a heavy diesel mechanical business with additional air con certificates, remapping engine rebuilt

Contact Information for Business Card

Company Name, Director Name, Managing Director, Contact details, email and website

Font styles to use
Serif
Script

```html
<!DOCTYPE html>
<html lang="en">
<head>
<meta charset="utf-8">
<title>Korvell Plant Services – Business Card</title>
<link href="https://fonts.googleapis.com/css2?family=Exo+2:wght@400;500;700&display=swap" rel="stylesheet">
<style>
  :root {
    --backdrop: #e9e9ec;
    --card-dark: #232323;
    --card-dark-edge: #2e2e2e;
    --card-light: #ffffff;
    --navy: #262a6e;
    --ink: #2a2a2a;
    --white: #ffffff;
  }
  * { box-sizing: border-box; margin: 0; padding: 0; }
  html, body { width: 1200px; height: 900px; overflow: hidden; }
  body {
    background: var(--backdrop);
    font-family: "Exo 2", sans-serif;
    position: relative;
  }
  .card {
    position: absolute;
    left: 300px;
    width: 600px;
    height: 343px;
    border-radius: 22px;
    box-shadow: 0 12px 30px rgba(0,0,0,0.18);
    overflow: hidden;
  }
  .card--front {
    top: 60px;
    background: linear-gradient(135deg, var(--card-dark-edge), var(--card-dark));
  }
  .card--back {
    top: 470px;
    background: var(--card-light);
  }
  .brand-name {
    font-weight: 700;
    line-height: 1.05;
  }
  .card--front .brand-name {
    position: absolute;
    right: 60px;
    top: 118px;
    width: 300px;
    text-align: right;
    color: var(--white);
    font-size: 42px;
  }
  .card--back .brand-name {
    position: absolute;
    right: 40px;
    top: 70px;
    width: 200px;
    text-align: right;
    color: var(--navy);
    font-size: 28px;
  }
  .holder {
    position: absolute;
    left: 40px;
    top: 92px;
  }
  .holder__name {
    color: var(--navy);
    font-weight: 700;
    font-size: 28px;
    letter-spacing: 0.5px;
  }
  .holder__title {
    color: var(--ink);
    font-size: 16px;
    margin-top: 2px;
  }
  .divider {
    position: absolute;
    left: 40px;
    right: 40px;
    top: 170px;
    height: 1px;
    background: var(--navy);
  }
  .contacts {
    position: absolute;
    left: 40px;
    top: 184px;
    list-style: none;
    color: var(--ink);
    font-size: 17px;
  }
  .contacts li {
    display: flex;
    align-items: center;
    gap: 10px;
    height: 28px;
  }
  .contacts svg { width: 13px; height: 13px; fill: var(--navy); }
  .address {
    position: absolute;
    right: 40px;
    bottom: 34px;
    text-align: right;
    color: var(--ink);
    font-size: 17px;
    line-height: 1.45;
  }
</style>
</head>
<body>
  <section class="card card--front" aria-label="Business card front">
    <p class="brand-name">Korvell<br>Plant Services</p>
  </section>

  <section class="card card--back" aria-label="Business card back">
    <div class="holder">
      <p class="holder__name">DORIAN HALE</p>
      <p class="holder__title">Managing Director</p>
    </div>
    <p class="brand-name">Korvell<br>Plant Services</p>
    <div class="divider"></div>
    <ul class="contacts">
      <li>
        <svg viewBox="0 0 16 16" aria-hidden="true"><path d="M3 1h3l1.5 4-2 1.5a9 9 0 0 0 4 4L11 8.5l4 1.5v3a2 2 0 0 1-2 2A12 12 0 0 1 1 3a2 2 0 0 1 2-2z"/></svg>
        555-014-2279
      </li>
      <li>
        <svg viewBox="0 0 16 16" aria-hidden="true"><path d="M1 3h14v10H1z M1 3l7 6 7-6" fill="none" stroke="#262a6e" stroke-width="1.6"/></svg>
        info@korvellplant.com
      </li>
      <li>
        <svg viewBox="0 0 16 16" aria-hidden="true"><circle cx="8" cy="8" r="7"/></svg>
        www.korvellplant.com
      </li>
    </ul>
    <p class="address">P.O. Box &nbsp;Street Name<br>Country Name AB, A5B 521</p>
  </section>
</body>
</html>
```